Vantor Glide - Stock Certificate

We need a custom designed stock certificate that represents the look of our company logo but also have a cool look compared to a standard stock certificate. We thinking we want the logo in gold. Our website is https://www.vantorglideusa.example.

We are wanting the certificate to look very professional and really cool, we have sales agents that work for the company and we are creating a program by which the sales agents can gain ownership in the company. So the certificates need to have a very cool appeal and that provides a sense of pride in owning "Units" in Vantor Glide.
Updates

Reason: Extending so other board members can vote as well, thank you all!

Target Market(s)

Stock/Shareholders

Industry/Entity Type

It Company

Font styles to use
Script

Requirements
Must have
• Must look like a stock certificate, must use our logo which the psd file for it was attached.
Nice to have
• Nice to have the logo in gold

```html
<!DOCTYPE html>
<html lang="en">
<head>
<meta charset="utf-8">
<title>Vantor Glide – Stock Certificate</title>
<link rel="stylesheet" href="https://fonts.googleapis.com/css2?family=UnifrakturCook:wght@700&family=Pinyon+Script&family=Great+Vibes&family=Dancing+Script:wght@400&family=Arimo:wght@400&family=Open+Sans:ital,wght@0,400;1,400&display=swap">
<style>
  :root {
    --paper: #ffffff;
    --map-light: #f3f3f3;
    --map-mid: #e6e6e6;
    --ink: #111111;
    --title-deep: #b8400c;
    --title-warm: #e4701c;
    --frame-orange: #e05f12;
    --frame-gold: #f7c21a;
    --fill-ink: #6b4a1a;
    --atom-core: #f2a12a;
    --atom-edge: #8a3008;
  }
  * { box-sizing: border-box; margin: 0; padding: 0; }
  html, body { width: 1200px; height: 795px; overflow: hidden; background: var(--paper); }
  .certificate {
    position: relative;
    width: 1200px;
    height: 795px;
    background: var(--paper);
    font-family: "Arimo", Arial, sans-serif;
    color: var(--ink);
  }
  .world-map {
    position: absolute;
    inset: 0;
    background: radial-gradient(ellipse at 55% 45%, var(--map-light) 0%, var(--map-mid) 100%);
  }
  .frame { position: absolute; inset: 0; }
  .corner-ornament {
    position: absolute;
    width: 96px;
    height: 96px;
  }
  .corner-ornament.top-left { left: 20px; top: 16px; background: var(--frame-orange); }
  .corner-ornament.top-right { right: 20px; top: 16px; background: var(--frame-orange); }
  .corner-ornament.bottom-left { left: 20px; bottom: 16px; background: var(--frame-orange); }
  .corner-ornament.bottom-right { right: 20px; bottom: 16px; background: var(--frame-orange); }

  .atom-illustration {
    position: absolute;
    left: 52px;
    top: 136px;
    width: 296px;
    height: 324px;
    border-radius: 50%;
    background: radial-gradient(circle at 50% 50%, #fff3c4 0%, var(--atom-core) 18%, rgba(200,90,20,0.55) 45%, rgba(138,48,8,0.18) 70%, rgba(255,255,255,0) 78%);
  }
  .brand-name {
    position: absolute;
    left: 92px;
    top: 500px;
    width: 240px;
    text-align: center;
    font-family: "Arimo", Arial, sans-serif;
    font-size: 38px;
    font-weight: 400;
    color: var(--ink);
    letter-spacing: 1px;
  }

  .title {
    position: absolute;
    left: 400px;
    top: 78px;
    width: 700px;
    text-align: center;
    font-family: "UnifrakturCook", serif;
    font-weight: 700;
    font-size: 86px;
    line-height: 1;
    background: linear-gradient(180deg, var(--title-warm) 0%, var(--title-deep) 100%);
    -webkit-background-clip: text;
    background-clip: text;
    color: transparent;
  }
  .body-text {
    position: absolute;
    left: 360px;
    width: 776px;
    text-align: center;
    font-size: 20px;
    line-height: 26px;
  }
  .certifies { top: 213px; }
  .holder-line {
    position: absolute;
    left: 512px;
    top: 290px;
    width: 478px;
    height: 76px;
    border-bottom: 1.5px solid var(--ink);
  }
  .holder-name {
    position: absolute;
    left: 0;
    right: 0;
    bottom: -14px;
    text-align: center;
    font-family: "Pinyon Script", cursive;
    font-size: 78px;
    line-height: 1;
    padding-left: 30px;
  }
  .entitlement { top: 393px; }
  .class-line { top: 419px; }
  .transfer { top: 472px; }
  .witness { top: 548px; }

  .blank {
    position: relative;
    display: inline-block;
    border-bottom: 1.5px solid var(--ink);
    height: 20px;
    vertical-align: baseline;
  }
  .blank.share-count { width: 52px; }
  .blank.par-value { width: 168px; }
  .blank.stock-class { width: 238px; }
  .fill {
    position: absolute;
    left: 0;
    right: 0;
    bottom: 1px;
    text-align: center;
    color: var(--fill-ink);
    line-height: 1;
  }
  .fill.numeral { font-family: "Dancing Script", cursive; font-size: 30px; }
  .fill.class-name { font-family: "Great Vibes", cursive; font-size: 24px; bottom: -4px; }

  .signature-block {
    position: absolute;
    top: 642px;
    width: 142px;
    height: 70px;
    border-bottom: 1.5px solid var(--ink);
  }
  .signature-block.left { left: 534px; }
  .signature-block.right { left: 812px; }
  .signature-mark {
    position: absolute;
    left: 8px;
    right: 8px;
    top: 14px;
    bottom: 6px;
    background: linear-gradient(90deg, rgba(0,0,0,0.04), rgba(0,0,0,0.12), rgba(0,0,0,0.04));
    border-radius: 40% 60% 50% 50%;
  }
  .signature-label {
    position: absolute;
    left: 0;
    right: 0;
    top: 73px;
    text-align: center;
    font-family: "Open Sans", sans-serif;
    font-style: italic;
    font-size: 21px;
    color: var(--ink);
  }
</style>
</head>
<body>
<main class="certificate">
  <div class="world-map" role="img" aria-label="Faint world map background"></div>

  <svg class="frame" width="1200" height="795" viewBox="0 0 1200 795" aria-hidden="true">
    <defs>
      <linearGradient id="frameGradient" x1="0" y1="0" x2="0" y2="1">
        <stop offset="0" stop-color="var(--frame-orange)"/>
        <stop offset="0.5" stop-color="var(--frame-gold)"/>
        <stop offset="1" stop-color="var(--frame-orange)"/>
      </linearGradient>
    </defs>
    <rect x="26" y="22" width="1148" height="751" fill="none" stroke="url(#frameGradient)" stroke-width="5"/>
  </svg>
  <div class="corner-ornament top-left" role="img" aria-label="Key-pattern corner ornament"></div>
  <div class="corner-ornament top-right" role="img" aria-label="Key-pattern corner ornament"></div>
  <div class="corner-ornament bottom-left" role="img" aria-label="Key-pattern corner ornament"></div>
  <div class="corner-ornament bottom-right" role="img" aria-label="Key-pattern corner ornament"></div>

  <div class="atom-illustration" role="img" aria-label="Glowing golden atom illustration with orbiting rings"></div>
  <div class="brand-name">Vantor Glide</div>

  <h1 class="title">Stock Certificate</h1>

  <p class="body-text certifies">This certifies that</p>

  <div class="holder-line">
    <span class="holder-name">John Doe</span>
  </div>

  <p class="body-text entitlement">is entitled to <span class="blank share-count"><span class="fill numeral">55</span></span> shares of the par value of <span class="blank par-value"><span class="fill numeral">120$</span></span>each of the</p>
  <p class="body-text class-line"><span class="blank stock-class"><span class="fill class-name">Common stock</span></span> &nbsp;of &nbsp;the &nbsp;Vantor Glide Company</p>

  <p class="body-text transfer">transferable in person or by Attorney only in the books of the Company and upon<br>the surrender of this Certificate.</p>

  <p class="body-text witness">In witness whereof the Vantor Glide Company &nbsp;has caused this Certificate to be</p>

  <div class="signature-block left">
    <div class="signature-mark" role="img" aria-label="Handwritten signature"></div>
    <span class="signature-label">Signature</span>
  </div>
  <div class="signature-block right">
    <div class="signature-mark" role="img" aria-label="Handwritten signature"></div>
    <span class="signature-label">Signature</span>
  </div>
</main>
</body>
</html>
```